Modern Label for cleaning products for the brand Voralux

We need a label design for our line of cleaning products. The label should feature our logo and an image to identify the product's intended use. I've added our logo and an image for use. This only concerns the design of the label on the front of the bottle.

Label dimensions:
Label 1 (500ml bottle with spray): width 58mm x height 115mm
Label 2: (1L bottle): width 73mm x height 140mm
The design must be consistent for both bottles which you find in the pictures.

The bottles to be labeled are white. See the attachment for a photo of the bottles.

The photo must also appear on the label to identify the product's intended use.

Product information:
Brand: Voralux
Product: Sanitary Cleaner

This text must be placed on the label:
"Cleans, descales & freshens. followed with this text: "Ideal for quick and powerful cleaning. A ready-to-use product for everyday use."

- Mention the seperate USP's: Sanitary, Bathroom, Toilet, Wet areas

Appearance: This is a consumer product, but it must have a professional appearance. We would like to see a design that use the color blue from our logo.

Target Market(s)

Consumers who take care of their homes and want to maintain it the correct (professional) way

Font styles to use
Sans Serif

Colors
0054AA
0677BA
7BADD7
CADEEF
E8F1F8

Requirements
Must have
• USP's + use of image and logo + blend in 1 design
Nice to have
• Keep the color of the logo in the design
Should not have
• Comic sans

```html
<!DOCTYPE html>
<html lang="en">
<head>
<meta charset="utf-8">
<title>Voralux Sanitary Cleaner – Front Label</title>
<link rel="stylesheet" href="https://fonts.googleapis.com/css2?family=Montserrat:ital,wght@0,400;0,600;0,700;1,500&family=Oswald:wght@700&display=swap">
<style>
  :root {
    --page-bg: #a3a6aa;
    --label-bg: #f4f5f6;
    --blue-deep: #0b3a8c;
    --blue-brand: #0054AA;
    --blue-mid: #0677BA;
    --blue-light: #7BADD7;
    --blue-pale: #CADEEF;
    --navy-title: #1c2670;
    --ink: #222327;
    --accent-red: #e01e2b;
    --silver: #c9ccd1;
  }
  * { margin: 0; padding: 0; box-sizing: border-box; }
  html, body { width: 900px; height: 1200px; overflow: hidden; }
  body {
    background: var(--page-bg);
    font-family: "Montserrat", sans-serif;
    position: relative;
  }
  .label {
    position: absolute;
    left: 170px; top: 45px;
    width: 560px; height: 1110px;
    border-radius: 22px;
    overflow: hidden;
    background: radial-gradient(ellipse at 50% 40%, #ffffff 0%, var(--label-bg) 60%, #e6e8ea 100%);
  }
  .label-header { position: absolute; left: 0; top: 0; width: 560px; height: 220px; }
  .brand-name {
    position: absolute; top: 212px; width: 100%;
    text-align: center;
    font-family: "Montserrat", sans-serif;
    font-weight: 600; font-size: 60px; letter-spacing: -1px;
    color: var(--ink);
  }
  .product-title {
    position: absolute; top: 292px; width: 100%;
    text-align: center;
    font-family: "Oswald", sans-serif;
    font-weight: 700; font-size: 92px; line-height: 1;
    color: var(--navy-title);
  }
  .product-subtitle {
    position: absolute; top: 392px; width: 100%;
    text-align: center;
    font-weight: 400; font-size: 38px; line-height: 1;
    letter-spacing: 25px; padding-left: 25px;
    color: var(--blue-mid);
  }
  .benefits {
    position: absolute; top: 448px; width: 100%;
    text-align: center;
    font-weight: 700; font-size: 27px;
    color: var(--ink);
  }
  .benefits-rule {
    position: absolute; top: 490px; left: 70px; width: 420px; height: 3px;
    background: linear-gradient(90deg, transparent, var(--accent-red) 15%, var(--accent-red) 85%, transparent);
  }
  .description {
    position: absolute; top: 512px; width: 100%;
    text-align: center;
    font-weight: 400; font-size: 23px; line-height: 34px;
    color: var(--ink);
  }
  .usage-photo {
    position: absolute; left: 0; top: 640px; width: 560px; height: 380px;
    background: linear-gradient(90deg, #8e8d8b 0%, #b9b7b3 28%, #eef0f2 50%, #e7e9eb 75%, #a9a8a6 100%);
  }
  .photo-frame { position: absolute; left: 0; top: 596px; width: 560px; height: 70px; }
  .usp-band {
    position: absolute; left: 0; top: 1018px; width: 560px; height: 92px;
    background: linear-gradient(90deg, var(--blue-deep), var(--blue-brand) 50%, var(--blue-deep));
    border-top: 4px solid var(--accent-red);
    color: #ffffff;
    text-align: center;
    font-style: italic; font-weight: 500; font-size: 28px; line-height: 35px;
    letter-spacing: 1px;
    padding-top: 8px;
  }
</style>
</head>
<body>
  <main class="label">
    <svg class="label-header" viewBox="0 0 560 220" aria-hidden="true">
      <defs>
        <linearGradient id="headerBlue" x1="0" y1="0" x2="1" y2="0">
          <stop offset="0" stop-color="#0b3a8c"/>
          <stop offset="0.5" stop-color="#0677BA"/>
          <stop offset="1" stop-color="#0b3a8c"/>
        </linearGradient>
      </defs>
      <path d="M0 0 H560 V70 L280 150 L0 70 Z" fill="url(#headerBlue)"/>
      <path d="M0 70 L280 150 L560 70 L560 92 L280 168 L0 92 Z" fill="#c9ccd1"/>
      <path d="M0 82 L280 160 L560 82" fill="none" stroke="#ffffff" stroke-width="3"/>
      <circle cx="280" cy="118" r="68" fill="#ffffff" stroke="#0054AA" stroke-width="10"/>
    </svg>

    <div class="brand-name">voralux</div>
    <h1 class="product-title">SANITARY</h1>
    <div class="product-subtitle">CLEANER</div>
    <p class="benefits">Cleans | Descales | Freshens</p>
    <div class="benefits-rule"></div>
    <p class="description">Ideal for quick and powerful cleaning.<br>A ready-to-use product for everyday use</p>

    <div class="usage-photo" role="img" aria-label="Photo of a modern bathroom with glass shower, washbasin and bathtub"></div>
    <svg class="photo-frame" viewBox="0 0 560 70" aria-hidden="true">
      <path d="M0 0 H560 V50 L280 4 L0 50 Z" fill="#f4f5f6"/>
      <path d="M0 50 L280 4 L560 50 L560 62 L280 16 L0 62 Z" fill="#c9ccd1"/>
    </svg>

    <div class="usp-band">Sanitary, Bathroom, Toilet<br>&amp; Wet areas</div>
  </main>
</body>
</html>
```